Tarnwick Nectar needs a great booklet

We need a booklet design for our Raw Honey business that is based in Dubai. Something clean and niche as our honey is special /very expensive. We have 12 types of honey and each type has its health benefits. As well we are very active on social media so will be good to be very creative and find a way through out this booklet to connect with the consumer. DO NOT inspire from the material i have send you (with the exception of wording)as this was done at the beginning of our business year so we would like something different.
I have attached the specs as we will be printing it in that format. We are looking to find a design source for future projects in various media formats.
Try to use a clean font and not funny ones (please try and find TARNWICK'S LOGO fonts)
For knowing more of who we are please have a look at our instagram account: tarnwicknectarae
THE FINAL DESIGN SHOULD LOOK LIKE A EDUCATIONAL BOOK FOR HONEY USERS BUT HAVE A PERSONAL FEEL. BE CREATIVE! HAVE FUN!
Updates

Please don't post anything that is similar to the options i got so far as it is a no for that kind. Added Wednesday, April 12, 2017

Industry/Entity Type

Business

Colors

Designer to choose colors to be used in the design.

Requirements
Must have
• a new look and please don't use the artwork/colors of the material i had send as that is to be used only for wording .
• File 1 - has the requirements for number of pages and size of booklet
Nice to have
• new and cool ideas
Should not have
• DO NOT inspire from the material i have send you (with the exception of wording)as this was done at the beginning of our business year so we would like something different.

```html
<!DOCTYPE html>
<html lang="en">
<head>
<meta charset="utf-8">
<title>Tarnwick Nectar Booklet – Pages 7–8</title>
<link rel="stylesheet" href="https://fonts.googleapis.com/css2?family=Alegreya+Sans:wght@400&family=Alegreya:ital@1&family=Roboto:wght@300&display=swap">
<style>
  :root {
    --backdrop: #dcdcdc;
    --paper: #ffffff;
    --heading: #4b3a2b;
    --quote: #8c6b4c;
    --body: #dcc0a6;
    --meta: #b9a390;
    --dots: #f8dcc2;
    --hex-pale: #fdf1ea;
    --hex-divider: #ece8e5;
    --photo-dark: #3a2e26;
    --photo-warm: #6e5a4a;
    --photo-light: #a8998c;
  }
  * { margin: 0; padding: 0; box-sizing: border-box; }
  html, body { width: 1200px; height: 1200px; overflow: hidden; }
  body { background: var(--backdrop); position: relative; }

  .spread {
    position: absolute; left: 50px; top: 222px;
    width: 1100px; height: 756px;
    background: var(--paper); overflow: hidden;
  }
  .dot-band { position: absolute; background: var(--dots); border-radius: 4px; }
  .dot-band--top-a { left: 0; top: 38px; width: 1050px; height: 8px; opacity: .7; }
  .dot-band--top-b { left: 40px; top: 50px; width: 720px; height: 8px; }
  .dot-band--top-c { left: 210px; top: 62px; width: 890px; height: 6px; opacity: .6; }
  .dot-band--bottom-a { left: 435px; top: 708px; width: 665px; height: 8px; opacity: .7; }
  .dot-band--bottom-b { left: 495px; top: 720px; width: 605px; height: 8px; }
  .dot-band--bottom-c { left: 700px; top: 732px; width: 400px; height: 6px; opacity: .6; }

  .site-url {
    position: absolute; left: 802px; top: 38px;
    padding: 0 6px; background: var(--paper);
    font: 300 17px/22px "Roboto", Helvetica, sans-serif;
    letter-spacing: .5px; color: var(--meta);
  }

  .entry { position: absolute; width: 450px; }
  .entry__title {
    font: 400 27px/34px "Alegreya Sans", sans-serif;
    color: var(--heading);
  }
  .entry__quote {
    margin-top: 2px;
    font: italic 18px/23px "Alegreya", serif;
    color: var(--quote);
  }
  .entry__body {
    margin-top: 10px;
    font: 300 15.5px/20.6px "Roboto", Helvetica, sans-serif;
    color: var(--body);
  }
  .entry--ginger { left: 55px; top: 132px; }
  .entry--vanilla { left: 55px; top: 413px; }
  .entry--pollen { left: 605px; top: 132px; }

  .hex-divider { position: absolute; left: 232px; top: 376px; }
  .page-number {
    position: absolute; left: 55px; top: 699px;
    font: 300 15px/20px "Roboto", Helvetica, sans-serif;
    letter-spacing: 2px; color: var(--meta);
  }
  .hex-row { position: absolute; left: 582px; top: 514px; }
</style>
</head>
<body>
  <main class="spread">
    <div class="dot-band dot-band--top-a"></div>
    <div class="dot-band dot-band--top-b"></div>
    <div class="dot-band dot-band--top-c"></div>
    <div class="site-url">WWW.TARNWICKNECTAR.CO</div>

    <section class="entry entry--ginger">
      <h2 class="entry__title">Raw Yemeni Honey infused<br>with Ginger</h2>
      <p class="entry__quote">“Ginger and raw honey for respiratory health.”</p>
      <p class="entry__body">This delicious mixture is capable of treating and relieving symptoms of asthma as well as other respiratory difficulties like cough, cold, sore throat and runny noses! Nature made the perfect treatment in a combination of Ginger and Tarnwick Raw Honey.</p>
    </section>

    <svg class="hex-divider" width="92" height="16" viewBox="0 0 92 16" aria-hidden="true">
      <g fill="var(--hex-divider)">
        <polygon points="4,1 12,1 16,8 12,15 4,15 0,8"/>
        <polygon points="23,1 31,1 35,8 31,15 23,15 19,8"/>
        <polygon points="42,1 50,1 54,8 50,15 42,15 38,8"/>
        <polygon points="61,1 69,1 73,8 69,15 61,15 57,8"/>
        <polygon points="80,1 88,1 92,8 88,15 80,15 76,8"/>
      </g>
    </svg>

    <section class="entry entry--vanilla">
      <h2 class="entry__title">Raw Yemeni Honey infused with<br>Vanilla Beans</h2>
      <p class="entry__quote">“Madagascar, Grade A Vanilla Beans and raw honey for cleansing and relaxation.”</p>
      <p class="entry__body">The World’s finest Madagascar vanilla beans infuses our Raw Yemeni Honey to create a smooth, rich flavor for any pairing. Wonderful drizzled over morning yogurt, added to cheese or matched to your favorite desert. Tarnwick Raw Yemeni Honey with Vanilla serves as an antioxidant, antidepressant, aphrodisiac, and as a delicious relaxant.</p>
    </section>

    <div class="page-number">11</div>

    <section class="entry entry--pollen">
      <h2 class="entry__title">Raw Yemeni Honey infused with<br>Bee Pollen</h2>
      <p class="entry__quote">“Bee Pollen and raw honey for total health.”</p>
      <p class="entry__body">As one of nature’s most completely nourishing foods, Pollen contains nearly all the nutrients that we require. Tarnwick mixes our Raw Yemeni Honey with the finest Bee Pollen to create a blend that improves endurance and vitality, prevents infectious diseases such as colds and flu (it has antibiotic type properties), aids in recovery from chronic illness, and extends longevity!</p>
    </section>

    <svg class="hex-row" width="518" height="166" viewBox="0 0 518 166">
      <polygon fill="var(--hex-pale)" points="72,0 144,41.5 144,124.5 72,166 0,124.5 0,41.5"/>
      <polygon fill="var(--photo-dark)" role="img" aria-label="Photo of honey jars with product labels" points="230,0 302,41.5 302,124.5 230,166 158,124.5 158,41.5"/>
      <polygon fill="var(--photo-warm)" role="img" aria-label="Photo of a honey jar beside scattered bee pollen" points="390,0 462,41.5 462,124.5 390,166 318,124.5 318,41.5"/>
      <polygon fill="var(--photo-light)" role="img" aria-label="Photo of bee pollen in a dish" points="548,0 620,41.5 620,124.5 548,166 476,124.5 476,41.5"/>
    </svg>

    <div class="dot-band dot-band--bottom-a"></div>
    <div class="dot-band dot-band--bottom-b"></div>
    <div class="dot-band dot-band--bottom-c"></div>
  </main>
</body>
</html>
```